Corwin Ashdale Building Company, Inc.
Business Cards, Letterhead, Envelopes, Fax Cover
Professional
Miles T. Fenwick
PO Box 48217
Raleigh, NC 27622
miles@corwinashdale-example.com
www.corwinashdale-example.com
looking for a traditional style card, however nothing dated. same goes for the stationary. Something that is creative , but still shows professionalism and adaptable to the corporate environment. We don't want gloss cards. waiting on office and fax #'s. should have those in a day or two. As for the font, I put use same as logo font, but may want to see standard as well.
CA

```html
<!DOCTYPE html>
<html lang="en">
<head>
<meta charset="utf-8">
<title>Corwin Ashdale Building Company – Business Card</title>
<link rel="stylesheet" href="https://fonts.googleapis.com/css2?family=Marcellus&display=swap">
<style>
  :root {
    --backdrop: #e9e4dc;
    --card: #ffffff;
    --navy: #27336b;
    --navy-deep: #1c2656;
    --silver: #c3c6cf;
    --ink: #3a3a3c;
    --muted: #8f93a3;
  }
  * { margin: 0; padding: 0; box-sizing: border-box; }
  html, body {
    width: 1200px; height: 893px; overflow: hidden;
    background: var(--backdrop);
  }
  .canvas { position: relative; width: 1200px; height: 893px; }
  .card {
    position: absolute; left: 206px; top: 222px;
    width: 788px; height: 449px;
    background: var(--card);
    border-radius: 22px;
    overflow: hidden;
    box-shadow: 0 6px 22px rgba(60, 45, 30, 0.18);
    font-family: "Marcellus", serif;
    color: var(--ink);
  }
  .card-band { position: absolute; left: 0; top: 0; width: 788px; height: 150px; }
  .holder-name {
    position: absolute; left: 150px; top: 44px;
    font-size: 34px; color: #fff; letter-spacing: 0.5px;
  }
  .holder-title {
    position: absolute; left: 316px; top: 86px;
    font-size: 13px; color: var(--silver); letter-spacing: 2px;
  }
  .divider {
    position: absolute; left: 410px; top: 160px;
    width: 2px; height: 225px;
    background: linear-gradient(to bottom, rgba(150,150,160,0), rgba(150,150,160,0.7) 50%, rgba(150,150,160,0));
  }
  .address {
    position: absolute; left: 53px; top: 180px;
    font-size: 24px; line-height: 41px; color: var(--ink);
  }
  .contact {
    position: absolute; left: 53px; top: 272px;
    font-size: 18px; line-height: 26.5px; color: var(--ink);
  }
  .contact .label { color: var(--navy); font-weight: bold; }
  .contact .label-lg { font-size: 21px; }
  .brand {
    position: absolute; left: 440px; top: 140px; width: 360px;
    text-align: center; color: var(--navy);
  }
  .brand-mark {
    display: block; width: 44px; height: 44px; margin: 0 auto 26px;
    background: var(--navy);
  }
  .brand-name { font-size: 34px; line-height: 38px; letter-spacing: 0.5px; }
  .brand-line { font-size: 24px; line-height: 32px; letter-spacing: 4px; }
  .web {
    position: absolute; left: 440px; top: 380px; width: 360px;
    text-align: center; font-size: 17px; font-weight: bold; color: var(--navy-deep);
  }
</style>
</head>
<body>
<div class="canvas">
  <div class="card">
    <svg class="card-band" viewBox="0 0 788 150" aria-hidden="true">
      <defs>
        <linearGradient id="swoosh" x1="0" x2="1" y1="0" y2="0">
          <stop offset="0" stop-color="#f4f4f6"/>
          <stop offset="0.45" stop-color="#b7bac4"/>
          <stop offset="1" stop-color="#e4e5ea"/>
        </linearGradient>
      </defs>
      <path d="M0 0 H788 V112 C700 100 560 96 440 118 C330 138 220 134 0 126 Z" fill="url(#swoosh)"/>
      <path d="M0 0 H788 V98 C700 88 560 84 440 106 C330 126 220 124 0 116 Z" fill="var(--navy)"/>
    </svg>
    <div class="holder-name">Miles T. Fenwick</div>
    <div class="holder-title">CEO</div>

    <div class="address">
      <div>1840 Harlow Avenue</div>
      <div>Raleigh, NC 27622</div>
    </div>
    <div class="contact">
      <div><span class="label">Tool Free</span> :888-555-0142</div>
      <div><span class="label">Phone</span> :919-555-0170</div>
      <div><span class="label">Fax</span> :919-555-0171</div>
      <div><span class="label label-lg">Email</span> :miles@corwinashdale-example.com</div>
    </div>

    <div class="divider"></div>

    <div class="brand">
      <span class="brand-mark"></span>
      <div class="brand-name">CORWIN ASHDALE</div>
      <div class="brand-line">BUILDING COMPANY</div>
    </div>
    <div class="web">http://www.corwinashdale-example.com</div>
  </div>
</div>
</body>
</html>
```